Need Eye Catching For Sale By Owner Signs

In need of a Eye Catching For Sale By Owner Sign design. I plan on using the sign to market buildings and raw land that I own. The design should be able to scale to different rectangular dimensions for example a yard stake sign or a large 4' x 6' sign to be tacked to plywood. The design should have a dead space near the bottom that I can insert more detail information into at a later time.

The main tag line "For Sale By Owner" and the contact number "318-562-4097" needs to be easily be read from a distance.

```html
<!DOCTYPE html>
<html lang="en">
<head>
<meta charset="utf-8">
<title>For Sale By Owner Signs</title>
<link rel="stylesheet" href="https://fonts.googleapis.com/css2?family=Roboto+Condensed:wght@700&display=swap">
<style>
  :root {
    --page-bg: #eeeeef;
    --slate-center: #5f6569;
    --slate-edge: #2c3034;
    --slate-corner: #a7aaad;
    --slate-stripe: #80858a;
    --slate-base-top: #f7f8f9;
    --slate-base-bottom: #d3d5d8;
    --rust-center: #d46c38;
    --rust-edge: #a54a29;
    --rust-corner: #f29a6c;
    --rust-stripe: #8f3b20;
    --rust-base-top: #fffbf8;
    --rust-base-bottom: #f6ebe4;
    --sign-text: #ffffff;
  }
  html, body {
    margin: 0;
    padding: 0;
    width: 1200px;
    height: 818px;
    overflow: hidden;
    background: var(--page-bg);
  }
  .canvas {
    position: relative;
    width: 1200px;
    height: 818px;
  }
  .sign {
    position: absolute;
    top: 96px;
    width: 386px;
    height: 578px;
    overflow: hidden;
  }
  .sign--slate { left: 188px; }
  .sign--rust { left: 625px; }
  .sign__art {
    position: absolute;
    inset: 0;
    width: 100%;
    height: 100%;
  }
  .sign__copy {
    position: absolute;
    inset: 0;
    color: var(--sign-text);
    font-family: "Roboto Condensed", "Arial Narrow", sans-serif;
    font-weight: 700;
    text-align: center;
    text-shadow: 0 2px 6px rgba(0, 0, 0, 0.25);
  }
  .sign__line {
    position: absolute;
    left: 0;
    right: 0;
    margin: 0;
    line-height: 1;
    white-space: nowrap;
  }
  .sign__for { top: 48px; font-size: 68px; }
  .sign__sale { top: 88px; font-size: 176px; letter-spacing: -4px; }
  .sign__owner { top: 242px; font-size: 69px; letter-spacing: -0.5px; }
  .sign__phone { top: 334px; font-size: 66px; letter-spacing: -0.5px; }
</style>
</head>
<body>
<main class="canvas">

  <section class="sign sign--slate" aria-label="For sale by owner sign, slate version">
    <svg class="sign__art" viewBox="0 0 321 482" preserveAspectRatio="none" aria-hidden="true">
      <defs>
        <radialGradient id="slate-field" cx="0.45" cy="0.4" r="0.75">
          <stop offset="0" stop-color="var(--slate-center)"/>
          <stop offset="1" stop-color="var(--slate-edge)"/>
        </radialGradient>
        <linearGradient id="slate-base" x1="0" y1="0" x2="0" y2="1">
          <stop offset="0" stop-color="var(--slate-base-top)"/>
          <stop offset="1" stop-color="var(--slate-base-bottom)"/>
        </linearGradient>
      </defs>
      <rect width="321" height="482" fill="url(#slate-field)"/>
      <polygon points="0,0 145,0 0,30" fill="var(--slate-corner)"/>
      <polygon points="0,400 321,326 321,340 0,412" fill="var(--slate-stripe)"/>
      <polygon points="0,412 321,340 321,482 0,482" fill="url(#slate-base)"/>
    </svg>
    <div class="sign__copy">
      <p class="sign__line sign__for">FOR</p>
      <p class="sign__line sign__sale">SALE</p>
      <p class="sign__line sign__owner">BY OWNER</p>
      <p class="sign__line sign__phone">318 562 4097</p>
    </div>
  </section>

  <section class="sign sign--rust" aria-label="For sale by owner sign, rust version">
    <svg class="sign__art" viewBox="0 0 321 482" preserveAspectRatio="none" aria-hidden="true">
      <defs>
        <radialGradient id="rust-field" cx="0.45" cy="0.45" r="0.75">
          <stop offset="0" stop-color="var(--rust-center)"/>
          <stop offset="1" stop-color="var(--rust-edge)"/>
        </radialGradient>
        <linearGradient id="rust-base" x1="0" y1="0" x2="0" y2="1">
          <stop offset="0" stop-color="var(--rust-base-top)"/>
          <stop offset="1" stop-color="var(--rust-base-bottom)"/>
        </linearGradient>
      </defs>
      <rect width="321" height="482" fill="url(#rust-field)"/>
      <polygon points="0,0 145,0 0,30" fill="var(--rust-corner)"/>
      <polygon points="0,400 321,326 321,340 0,412" fill="var(--rust-stripe)"/>
      <polygon points="0,412 321,340 321,482 0,482" fill="url(#rust-base)"/>
    </svg>
    <div class="sign__copy">
      <p class="sign__line sign__for">FOR</p>
      <p class="sign__line sign__sale">SALE</p>
      <p class="sign__line sign__owner">BY OWNER</p>
      <p class="sign__line sign__phone">318 562 4097</p>
    </div>
  </section>

</main>
</body>
</html>
```